use my brand and make an elegant business card  with it

Target Market(s)
male and female ' ages 25 to 45 age- who appreciate the highest quality goods, experiences, services, brands and relationships
Industry/Entity Type
Business
Requirements
Must have
- my logo integrated into the design-note the uploaded file
front: just logo and the phrase: New. Trend. Life. Style
back informations:
Mirela Dostan
Director
phone: +1 604 5290417
www.midostan.com
email: mireladostan@midostan.com
the pin of Facebook (F) and tweeter (T)
Nice to have
- contrast of the colors black gold and silver
Should not have
- cartoons or whimsical design

```html
<!DOCTYPE html>
<html lang="en">
<head>
<meta charset="utf-8">
<title>Mi Dostan — Business Card</title>
<link rel="stylesheet" href="https://fonts.googleapis.com/css2?family=Mulish:ital,wght@0,400;0,700;1,400&display=swap">
<style>
  :root {
    --backdrop: #e6e7e8;
    --card-black: #000000;
    --gold: #b98b0b;
    --silver: #77787b;
    --silver-text: #808184;
  }
  * { box-sizing: border-box; margin: 0; padding: 0; }
  html, body {
    width: 1200px; height: 1000px; overflow: hidden;
    background: var(--backdrop);
    font-family: "Mulish", sans-serif;
  }
  .card {
    position: absolute;
    width: 580px; height: 334px;
    background: var(--card-black);
    overflow: hidden;
  }
  .card--front { left: 156px; top: 120px; }
  .card--back { left: 466px; top: 546px; }
  .card__decor { position: absolute; inset: 0; width: 100%; height: 100%; }

  .brand-name {
    position: absolute; left: 86px; top: 118px;
    font-size: 70px; font-weight: 700; letter-spacing: 2px;
    color: var(--gold); line-height: 1;
  }
  .tagline {
    position: absolute; left: 92px; top: 236px;
    font-size: 31px; font-weight: 400; color: var(--silver-text);
    letter-spacing: 0.3px;
  }

  .person { position: absolute; left: 91px; top: 42px; }
  .person__name { font-size: 21px; font-weight: 700; color: var(--gold); line-height: 1.2; }
  .person__role { font-size: 17px; font-style: italic; color: var(--silver-text); line-height: 1.3; }

  .contacts { position: absolute; left: 91px; top: 127px; list-style: none; }
  .contacts__item {
    display: flex; align-items: center; gap: 14px;
    height: 35px; font-size: 17.5px; color: var(--gold);
  }
  .contacts__icon { width: 22px; height: 22px; flex: none; }
</style>
</head>
<body>

<section class="card card--front">
  <svg class="card__decor" viewBox="0 0 580 334">
    <path role="img" aria-label="Gold leaf flourish along the left edge" fill="var(--gold)"
      d="M0 0 H28 Q70 60 62 150 Q50 230 60 300 L0 300 Z"/>
    <path role="img" aria-label="Silver leaf flourish in the lower right corner" fill="var(--silver)"
      d="M424 334 Q500 290 520 250 Q560 220 580 160 V334 Z"/>
  </svg>
  <div class="brand-name">MI DOSTAN</div>
  <p class="tagline">New. Trend. Life. Style</p>
</section>

<section class="card card--back">
  <svg class="card__decor" viewBox="0 0 578 334">
    <path role="img" aria-label="Gold leaf flourish along the left edge" fill="var(--gold)"
      d="M0 0 H28 Q70 60 62 150 Q50 230 60 300 L0 300 Z"/>
    <path role="img" aria-label="Silver leaf flourish in the lower right corner" fill="var(--silver)"
      d="M422 334 Q500 290 518 250 Q556 220 578 150 V334 Z"/>
  </svg>

  <div class="person">
    <p class="person__name">Mirela Dostan</p>
    <p class="person__role">Director</p>
  </div>

  <ul class="contacts">
    <li class="contacts__item">
      <svg class="contacts__icon" viewBox="0 0 22 22" aria-hidden="true">
        <circle cx="11" cy="11" r="11" fill="var(--silver)"/>
        <path d="M7.5 5.5 L9.5 5 L10.5 8 L9.2 9 Q10 11.5 12.8 12.8 L13.8 11.5 L16.8 12.5 L16.3 14.5 Q14 16.5 10.5 14 Q6.5 10.5 7.5 5.5 Z" fill="var(--card-black)"/>
      </svg>
      +1 604 5290417
    </li>
    <li class="contacts__item">
      <svg class="contacts__icon" viewBox="0 0 22 22" aria-hidden="true">
        <circle cx="11" cy="11" r="11" fill="var(--silver)"/>
        <g fill="none" stroke="var(--card-black)" stroke-width="1.2">
          <circle cx="11" cy="11" r="6"/>
          <ellipse cx="11" cy="11" rx="2.6" ry="6"/>
          <line x1="5" y1="11" x2="17" y2="11"/>
          <line x1="6" y1="8" x2="16" y2="8"/>
          <line x1="6" y1="14" x2="16" y2="14"/>
        </g>
      </svg>
      www.midostan.com
    </li>
    <li class="contacts__item">
      <svg class="contacts__icon" viewBox="0 0 22 22" aria-hidden="true">
        <circle cx="11" cy="11" r="11" fill="var(--silver)"/>
        <rect x="5.5" y="7" width="11" height="8" fill="var(--card-black)"/>
        <path d="M5.5 7 L11 11.5 L16.5 7" fill="none" stroke="var(--silver)" stroke-width="1.1"/>
      </svg>
      mireladostan@midostan.com
    </li>
    <li class="contacts__item">
      <svg class="contacts__icon" viewBox="0 0 22 22" aria-hidden="true">
        <circle cx="11" cy="11" r="11" fill="var(--silver)"/>
      </svg>
      mireladostan
    </li>
    <li class="contacts__item">
      <svg class="contacts__icon" viewBox="0 0 22 22" aria-hidden="true">
        <circle cx="11" cy="11" r="11" fill="var(--silver)"/>
      </svg>
      mireladostan
    </li>
  </ul>
</section>

</body>
</html>
```